Harwell Construct, LLC Business Card
Business Car Design
Harwell Construct, LLC Business Card - Construction
Creative Brief
Professional
Tom Morrow
Owner
P.O. Box 5817 Bluffton, SC 29910
tmorrow@harwellconstructsc.example
www.harwellconstructsc.example
Back of Business Card should be just the logo that fills up the page.

```html
<!DOCTYPE html>
<html lang="en">
<head>
<meta charset="utf-8">
<title>Harwell Construct, LLC – Stationery</title>
<link href="https://fonts.googleapis.com/css2?family=Libre+Baskerville&family=Open+Sans:wght@400;600&display=swap" rel="stylesheet">
<style>
  :root {
    --backdrop: #a9aaad;
    --paper: #ffffff;
    --brown: #4a3a33;
    --swoosh: #c9cacc;
    --ink: #3d302a;
    --muted: #6d625c;
  }
  * { margin: 0; padding: 0; box-sizing: border-box; }
  html, body { width: 1200px; height: 626px; overflow: hidden; }
  body { background: var(--backdrop); position: relative; font-family: "Open Sans", sans-serif; color: var(--ink); }

  .sheet { position: absolute; background: var(--paper); overflow: hidden; box-shadow: 0 1px 3px rgba(0,0,0,.25); }
  .sheet svg.edge { position: absolute; inset: 0; width: 100%; height: 100%; }

  .brand-name {
    font-family: "Libre Baskerville", serif;
    font-weight: 400;
    color: var(--brown);
    text-align: center;
    line-height: 1.1;
    position: absolute;
    left: 0; right: 0;
  }
  .brand-name .line { display: block; }
  .brand-name .line-small { display: block; font-size: .42em; letter-spacing: .25em; margin-top: .3em; }

  .card { width: 182px; height: 99px; left: 34px; border-radius: 8px; }
  .card-front { top: 199px; }
  .card-front .brand-name { top: 30px; font-size: 17px; }
  .card-back { top: 310px; }
  .card-back .contact { position: absolute; left: 0; right: 0; top: 16px; text-align: center; font-size: 6px; line-height: 1.5; color: var(--muted); }
  .card-back .contact .person { font-family: "Libre Baskerville", serif; font-size: 8px; color: var(--ink); }
  .card-back .contact .role { margin-bottom: 4px; }

  .letterhead { left: 233px; top: 29px; width: 434px; height: 566px; }
  .letterhead .brand-name { top: 28px; font-size: 19px; right: 30px; }
  .footer-line { position: absolute; font-size: 4.6px; color: var(--muted); white-space: nowrap; }
  .letterhead .footer-line { left: 50px; bottom: 16px; }

  .envelope { left: 679px; width: 490px; }
  .envelope-back { top: 79px; height: 204px; }
  .envelope-front { top: 336px; height: 216px; }
  .envelope-front .brand-name { top: 26px; font-size: 19px; }
  .envelope-front .footer-line { left: 90px; bottom: 30px; }
</style>
</head>
<body>

  <section class="sheet card card-front" aria-label="Business card front">
    <div class="brand-name"><span class="line">HARWELL</span><span class="line-small">CONSTRUCT, LLC</span></div>
  </section>

  <section class="sheet card card-back" aria-label="Business card back">
    <svg class="edge" viewBox="0 0 182 99" preserveAspectRatio="none" aria-hidden="true">
      <path d="M0 99 V76 Q90 96 182 74 V99 Z" fill="var(--swoosh)"/>
      <path d="M0 99 V82 Q90 100 182 80 V99 Z" fill="var(--brown)"/>
    </svg>
    <div class="contact">
      <div class="person">Tom Morrow</div>
      <div class="role">Owner</div>
      <div>P.O. Box 5817 Bluffton, SC 29910 &nbsp;·&nbsp; Cell: 843.555.0198</div>
      <div>tmorrow@harwellconstructsc.example</div>
      <div>www.harwellconstructsc.example</div>
    </div>
  </section>

  <section class="sheet letterhead" aria-label="Letterhead">
    <svg class="edge" viewBox="0 0 434 566" preserveAspectRatio="none" aria-hidden="true">
      <path d="M374 0 Q396 300 404 566 H414 Q406 300 388 0 Z" fill="var(--swoosh)"/>
      <path d="M388 0 Q406 300 414 566 H434 V0 Z" fill="var(--brown)"/>
    </svg>
    <div class="brand-name"><span class="line">HARWELL</span><span class="line-small">CONSTRUCT, LLC</span></div>
    <p class="footer-line">Phone: 843.555.0142 &nbsp;|&nbsp; Fax: 843.555.0143 &nbsp;|&nbsp; P.O. Box 5817 Bluffton, SC 29910 &nbsp;|&nbsp; tmorrow@harwellconstructsc.example &nbsp;|&nbsp; www.harwellconstructsc.example</p>
  </section>

  <section class="sheet envelope envelope-back" aria-label="Envelope back">
    <svg class="edge" viewBox="0 0 490 204" preserveAspectRatio="none" aria-hidden="true">
      <path d="M0 70 Q245 92 490 58 V66 Q245 100 0 80 Z" fill="var(--swoosh)"/>
      <path d="M0 0 H490 V58 Q245 92 0 70 Z" fill="var(--brown)"/>
    </svg>
  </section>

  <section class="sheet envelope envelope-front" aria-label="Envelope front">
    <svg class="edge" viewBox="0 0 490 216" preserveAspectRatio="none" aria-hidden="true">
      <path d="M0 0 H44 Q18 100 10 216 H0 Z" fill="var(--brown)"/>
      <path d="M44 0 H54 Q26 100 18 216 H10 Q18 100 44 0 Z" fill="var(--swoosh)"/>
      <path d="M490 50 Q476 140 452 216 H490 Z" fill="var(--brown)"/>
      <path d="M490 40 Q470 140 442 216 H452 Q476 140 490 50 Z" fill="var(--swoosh)"/>
    </svg>
    <div class="brand-name"><span class="line">HARWELL</span><span class="line-small">CONSTRUCT, LLC</span></div>
    <p class="footer-line">P.O. Box 5817 Bluffton, SC 29910 &nbsp;|&nbsp; tmorrow@harwellconstructsc.example &nbsp;|&nbsp; www.harwellconstructsc.example</p>
  </section>

</body>
</html>
```